Nectarine Point of Sale Cards for Grocery Retail Markets

We are looking to update our Nectarine point of sale card and price card. The cards will need to be 7" x 11" with a .125 bleed - one sided. See attached for the old versions. We would like this to use photos that look like true Washington State Peaches. Here are the bullet points we would like to use: - New Crop!- Tree Ripened- Excellent FlavorNOTE: The price card just needs to have a space where a retailer can write in the sale price of the item. See attachment with the white box.

Target Market(s)

Retail market shoppers

Requirements
Must have
• Pictures of Nectarines Only

```html
<!DOCTYPE html>
<html lang="en">
<head>
<meta charset="utf-8">
<title>Nectarine Point of Sale Card</title>
<link rel="stylesheet" href="https://fonts.googleapis.com/css2?family=Kaushan+Script&family=Open+Sans:wght@400;700&display=swap">
<style>
  :root {
    --leaf-green: #3d9a3a;
    --leaf-green-light: #5bb257;
    --brand-green: #2f7d34;
    --paper-white: #ffffff;
    --mist-white: rgba(255, 255, 255, 0.82);
    --swoosh-grey: #d9d9d9;
    --fruit-orange: #f08a2c;
    --page-bg: #eeeeee;
  }
  * { margin: 0; padding: 0; box-sizing: border-box; }
  html, body { width: 1200px; height: 777px; overflow: hidden; background: var(--page-bg); }
  .pos-card {
    position: relative;
    width: 1200px;
    height: 777px;
    overflow: hidden;
    background: var(--leaf-green);
  }
  .card-art { position: absolute; inset: 0; }
  .brand {
    position: absolute;
    left: 70px;
    top: 78px;
    display: flex;
    align-items: center;
    gap: 18px;
  }
  .brand-dot {
    width: 74px;
    height: 74px;
    border-radius: 50%;
    background: var(--fruit-orange);
  }
  .brand-name {
    font-family: "Open Sans", sans-serif;
    font-weight: 700;
    font-size: 30px;
    line-height: 1.05;
    color: var(--brand-green);
  }
  .headline-group {
    position: absolute;
    left: 250px;
    top: 300px;
    white-space: nowrap;
    transform: rotate(-12deg);
    transform-origin: center;
    color: var(--paper-white);
  }
  .headline {
    font-family: "Kaushan Script", cursive;
    font-weight: 400;
    font-size: 72px;
    line-height: 1.1;
    text-shadow: 0 2px 6px rgba(0, 0, 0, 0.25);
  }
  .subline {
    font-family: "Open Sans", sans-serif;
    font-weight: 400;
    font-size: 26px;
    line-height: 1.2;
    margin-top: 2px;
    margin-left: 160px;
  }
  .selling-points {
    position: absolute;
    left: 80px;
    top: 560px;
    list-style: none;
    transform: rotate(-6deg);
    transform-origin: left top;
  }
  .selling-points li {
    display: flex;
    align-items: center;
    gap: 34px;
    font-family: "Kaushan Script", cursive;
    font-size: 40px;
    color: var(--paper-white);
    height: 66px;
  }
  .selling-points li::before {
    content: "";
    width: 24px;
    height: 24px;
    border-radius: 50%;
    background: var(--paper-white);
    flex: none;
  }
  .selling-points li:nth-child(2) { margin-left: 18px; }
  .selling-points li:nth-child(3) { margin-left: 36px; }
  .price-box {
    position: absolute;
    right: 0;
    bottom: 0;
    width: 480px;
    height: 300px;
    background: var(--paper-white);
    border-top-left-radius: 46px;
  }
</style>
</head>
<body>
  <main class="pos-card">
    <svg class="card-art" width="1200" height="777" viewBox="0 0 1200 777" xmlns="http://www.w3.org/2000/svg">
      <defs>
        <linearGradient id="fruitPhotoTone" x1="0" y1="0" x2="1" y2="1">
          <stop offset="0" stop-color="#d9c3b8"/>
          <stop offset="0.35" stop-color="#f2a062"/>
          <stop offset="0.6" stop-color="#e8743e"/>
          <stop offset="1" stop-color="#8a6a58"/>
        </linearGradient>
        <radialGradient id="greenGlow" cx="0.3" cy="0.9" r="0.6">
          <stop offset="0" stop-color="#5bb257" stop-opacity="0.6"/>
          <stop offset="1" stop-color="#3d9a3a" stop-opacity="0"/>
        </radialGradient>
      </defs>
      <rect class="green-field" x="0" y="0" width="1200" height="777" fill="var(--leaf-green)"/>
      <circle class="green-glow" cx="300" cy="780" r="380" fill="url(#greenGlow)"/>
      <path class="swoosh-line" d="M0,508 Q760,568 1200,305 V318 Q760,584 0,522 Z" fill="var(--swoosh-grey)"/>
      <path class="fruit-photo" role="img" aria-label="Photo of ripe whole and halved nectarines with mint leaves on a wooden table"
            d="M0,0 H1200 V300 Q760,560 0,504 Z" fill="url(#fruitPhotoTone)"/>
      <path class="brand-mist" d="M0,0 H560 Q600,160 470,250 Q300,330 0,300 Z" fill="var(--mist-white)"/>
    </svg>

    <div class="brand">
      <span class="brand-dot"></span>
      <span class="brand-name">Cascade Valley<br>Fruit Board</span>
    </div>

    <div class="headline-group">
      <h1 class="headline">Taste The Difference!</h1>
      <p class="subline">Washington State Peaches</p>
    </div>

    <ul class="selling-points">
      <li>New Crop!</li>
      <li>Tree Ripened</li>
      <li>Excellent Flavor</li>
    </ul>

    <div class="price-box" aria-label="Space for sale price"></div>
  </main>
</body>
</html>
```